SaaS / Consulting / Solution website redesign

We need a website design that:
- Is completely different than our current design : https://velmorahub.com
- Has a very minimal amount of copy
- Changes our positioning from a SaaS application to a solutions company. Solutions company means that we help our customers solve their problems with consulting, training, and tools. An example of a solutions company is here: https://pastcache.net/web/20130111103320/http://www.quintorabuild.com:80/
- Does not make us look like a start up
- Is more people oriented than technology oriented

We need a designer that:
- Is a rebel at heart
- Is a minimalist
- Tells us why our current site sucks
- Can disagree with us
- Can also do copywriting or already has a copywriter that can help
- Is ok with saying we have capability that we don't in order to see if people actually want that
- Can understand the difference between our grand vision and where we need to focus ourselves today in order to get there

Who we are:
- Entrepreneurs
- Programmers
- Consultants
- Investors

Here's our design goals:
#1 Get customers, investors, employers, and partners excited about our unique and clearly articulated value proposition
#2 Get people to contact us asking for help with their programs
#3 Position ourselves as an expert in the skills based volunteering, mentorship, and group collaboration
#4 Make it easy for people, who already know who we are, to register online

What our grand vision is:
- Create a marketplace where any person can go to our site and find time with anyone they need to meet with. Whether that is their hair stylist, school advisor, parent of your kids class, dentist, attorney, etc.

What will you get if you win:
- In addition to the prize of this project we will have many landing pages and other revisions we will need in the future. We currently don't have a designer or copywriter and need to add that capability to our team

Who do we need to appeal to:
- Directors that are launching innovative programs inside organizations
- IT personnel who are trying to disqualify our technology so they don't have to support it or deal with it when it doesn't go well
- Enterprise IT architects who don't want our product being on its own island within their organization totally incompatible with everything else. Architects which are trying to assess how our platform will co-exist with all their other platforms
- Vice Presidents who want to help their directors understand that we don't have enough experience to help them
- Program managers who have to juggle a million things and need a tool that actually helps instead of confuses them and adds more work for them.
- Program managers & directors that have been given ambiguous goals by their board of directors like "improve retention, increase engagement, create innovation, get people to collaborate." And who have no idea where to start or how to deliver on things like that.
- Program managers, directors, and vice presidents that are trying to understand how our technology and services fit into their existing technology and capability
- Employees who are bored and uninspired with their current tools and are hoping for some excitement in their life. Kind of like candy or a double espresso.
- Investors who think, our company like all the rest, are going to waste their money and make them look like a fool

Other information:
-The CSS and html needs to be responsive

-Our registration onboarding flow needs to collect this information:
User first name
user last name
user email
(verify their email)
user phone number
(verify their phone number)
User profile image (optional)
User profile summary (optional, like a bio, freeform text fiels)
If applicable: Register their organization
Organization name
Organization image (optional)
Account Mailing address
account Billing address (could be same as mailing address)
account Billing email address (could be same as user address)
account Product selection (pricing tier)
account Credit card information

The designs I am getting are a good start but they are only the front page. I just want you to know that I am expecting and need more than a landing page to complete the design. I will likely need a page that outlines the benefits and features of the product itself, how its different than our competitors, which will not be on the front page. I will need a registration flow. I will need a blog page design so we can post blog articles, I will need a team page, a page that goes into detail on our training, our services. I will likely need a page that shows all news and media we have been in. I need to show customer and user quotes, case studies, a way to contact us, partners, general resources like on collaboration, product tutorials, customers. I need the site to address a comprehensive set of needs. I need that design to be consistent and thorough. I know what LayoutBazaar is. I'm not using because I need more than a template that was customized. I need to be unique and match our brand thoughtfully, beautifully, and artistically. Someone asked me a question about how Brindle is similar to our tool in the way it is referred by end users and purchased by managers. Our website needs to primarily talk to the managers as I explained in the brief but it needs to appear cool and exciting to our end-users without focusing on the technology too much. Brindle is a tool that teams use to collaborate in small and large enterprises. The value prop for them is that communication is easier. But they don't put that on their website. Why? Because the users of the technology won't go to the website to find out information on it, they get their information from someone who is using it and demos it to them. When Nadia tells her manager Ted "Lets get brindle, Olga is using it at her company and its great" Nadia's manager doesn't know anything about brindle so she promptly googles it. The most important thing from Nadia's perspective is that Ted agrees to try it out. Ted's biggest concern is that productivity will be enhanced to degraded. Brindle knows this and so on the front page they know they are talking to Ted NOT Nadia because Nadia is already sold on it and doesn't need to get sold on the website. Nadia is end user. Ted is the purchaser. We have the same problem and so our end users are not the ones purchasing our product, their managers are purchasing our product. We get referred by our end users and vetted by their managers. Hope this helps! Thank you for looking at this project!  Added Wednesday, June 7, 2017

Another observation I am having about the designs being submitted. I believe we used the animations on our current website because animations / cartoons connect with the "inner child" in our users. Whatever that means :-). I think it's what makes our brand fun. I have a hard time imagining that we could make the design fun looking without animations but I'm sure it can be achieved. I also recognize that blending pictures of real people and animations is hard. So either we must masterfully blend them, use only animations, or make the real people have a LOT of fun! So far most of the designs while achieve the goal of appealing to the serious Vice Presidents and directors, they are not doing a good job at appealing to the overworked program managers and bored employees. There seems to stand another challenge with animations which is animations are hard to find and/or create that achieve the message / emotion we are trying to communicate. I don't have any good answers for this but I will say we can hire both animators and illustrators if we need to. All you have to do is communicate the effect in the website design with some simpler version maybe not the end illustration or animation itself. Added Wednesday, June 7, 2017

Industry/Entity Type

Saas

Coding

Coded - Design and coding required

Number of Pages Required

5+ page

Font styles to use
Sans Serif

Requirements
Must have
• Sex appeal and a sense of humor. Copy that makes people excited and clairvoyant about our potential.
Should not have
• Boring renditions of other non-inspiring websites

```html
<!DOCTYPE html>
<html lang="en">
<head>
<meta charset="utf-8">
<title>Velmora</title>
<link href="https://fonts.googleapis.com/css2?family=Montserrat:wght@400;500;600;700&family=Mulish:wght@400;600;700&display=swap" rel="stylesheet">
<style>
:root{
  --ink:#333333;
  --muted:#6b6b6b;
  --accent:#2bb6ee;
  --yellow:#f5d547;
  --footer:#4a4a4a;
  --card:#e8e8e8;
  --blue-band:#18a8e0;
  --red:#ef5a56;
  --green:#43b862;
  --white:#ffffff;
}
*{margin:0;padding:0;box-sizing:border-box}
html,body{width:1200px;height:3066px;overflow:hidden}
body{position:relative;background:var(--white);font-family:"Mulish",sans-serif;color:var(--ink)}
.abs{position:absolute}
a{color:inherit;text-decoration:none}

/* hero */
.hero{position:absolute;left:0;top:0;width:1200px;height:650px;clip-path:polygon(0 0,100% 0,100% 590px,0 650px)}
.hero-photo{position:absolute;inset:0;background:linear-gradient(100deg,#3a2f28 0%,#6b5646 30%,#8a7a6c 55%,#4d4038 80%,#2d2622 100%)}
.hero-shade{position:absolute;inset:0;background:rgba(0,0,0,.25)}
.topbar{position:absolute;left:0;top:0;width:1200px;height:80px;background:rgba(30,30,30,.55)}
.logo{position:absolute;left:86px;top:19px;font-family:"Montserrat",sans-serif;font-weight:500;font-size:30px;color:var(--white);letter-spacing:.5px}
.nav a{position:absolute;top:31px;font-family:"Montserrat",sans-serif;font-size:13px;color:var(--white)}
.login{position:absolute;left:1036px;top:22px;width:78px;height:36px;border:1px solid var(--yellow);border-radius:2px;color:var(--yellow);font-family:"Montserrat",sans-serif;font-size:13px;display:flex;align-items:center;justify-content:center}
.hero-title{position:absolute;right:86px;top:256px;font-family:"Montserrat",sans-serif;font-weight:700;font-size:42px;color:var(--yellow);letter-spacing:.5px}
.hero-text{position:absolute;right:86px;top:316px;width:520px;text-align:right;color:var(--white);font-size:13.5px;line-height:20px;font-weight:600}
.btn{position:absolute;height:50px;display:flex;align-items:center;justify-content:center;font-family:"Montserrat",sans-serif;font-size:15px;font-weight:500;color:var(--white);letter-spacing:.5px}
.btn-signup{left:809px;top:401px;width:150px;background:var(--accent)}
.btn-contact{left:971px;top:401px;width:143px;border:1.5px solid var(--white)}
.dots{position:absolute;left:562px;top:571px;display:flex;gap:6px;align-items:center}
.dots span{width:10px;height:10px;border-radius:50%;background:var(--white)}
.dots .on{width:30px;border-radius:5px;background:var(--yellow)}

/* section titles */
.section-title{position:absolute;left:0;width:1200px;text-align:center;font-family:"Montserrat",sans-serif;font-weight:600;font-size:31px;color:var(--ink)}
.title-rule{position:absolute;left:535px;width:130px;height:3px;background:var(--accent)}

/* about */
.about-copy{position:absolute;left:190px;top:786px;width:820px;text-align:center;font-size:13px;line-height:22px;color:var(--muted)}
.about-copy p+p{margin-top:14px}
.btn-more{left:525px;top:1043px;width:150px;height:51px;background:var(--accent)}

/* we are */
.we-are{position:absolute;left:0;top:1155px;width:1200px;height:838px;clip-path:polygon(0 0,100% 92px,100% 100%,0 736px);background:radial-gradient(ellipse at 50% 45%,#2a2f33 0%,#1d2023 60%,#141618 100%)}
.we-are .section-title{color:var(--white)}
.quote-lead{position:absolute;left:200px;top:226px;width:800px;text-align:center;color:#e6e6e6;font-size:17px;line-height:27px}
.role{position:absolute;top:320px;width:250px;text-align:center;color:var(--white)}
.role-badge{width:164px;height:164px;border-radius:50%;border:3px solid var(--white);margin:0 auto;position:relative}
.role-badge::after{content:"";position:absolute;inset:8px;border-radius:50%;border:2px solid rgba(255,255,255,.85)}
.role-badge svg{position:absolute;left:42px;top:42px}
.role h3{margin-top:26px;font-family:"Montserrat",sans-serif;font-weight:600;font-size:16.5px;letter-spacing:.5px}
.role p{margin-top:6px;font-size:13px;line-height:20px;font-weight:600}
.role a{display:inline-block;margin-top:14px;font-size:12.5px;text-decoration:underline;font-weight:600}

/* blog */
.blog-card{position:absolute;top:2120px;width:241px;height:282px;background:var(--card)}
.blog-photo{height:159px}
.blog-card h4{margin:16px 16px 0;font-family:"Montserrat",sans-serif;font-weight:600;font-size:12.5px;line-height:18px;color:var(--ink)}
.blog-meta{position:absolute;left:16px;right:16px;bottom:22px;display:flex;justify-content:space-between;font-size:10.5px;color:#888}

/* testimonial */
.testimonial{position:absolute;left:0;top:2473px;width:1200px;height:399px;background:var(--blue-band);clip-path:polygon(0 82px,100% 0,100% 100%,0 100%)}
.avatar{position:absolute;left:90px;top:176px;width:126px;height:126px;border-radius:50%;border:4px solid var(--white);background:radial-gradient(circle at 50% 40%,#d9b49a,#7a5a48)}
.divider{position:absolute;left:255px;top:176px;width:1px;height:126px;background:rgba(255,255,255,.7)}
.testimonial blockquote{position:absolute;left:290px;top:180px;width:860px;color:var(--white);font-style:italic;font-size:14.5px;line-height:29px;font-weight:600}
.testimonial cite{position:absolute;left:290px;top:282px;color:var(--white);font-style:normal;font-family:"Montserrat",sans-serif;font-size:17px;font-weight:500}

/* footer */
.footer{position:absolute;left:0;top:2872px;width:1200px;height:194px;background:var(--footer);color:#cfcfcf}
.social{position:absolute;left:562px;top:50px;display:flex;gap:14px}
.social span{width:16px;height:16px;border-radius:50%;background:#9a9a9a}
.footer-nav{position:absolute;top:93px;font-family:"Montserrat",sans-serif;font-size:12.5px}
.copyright{position:absolute;left:0;width:1200px;top:134px;text-align:center;font-size:11px;color:#bdbdbd}
</style>
</head>
<body>

<header class="hero">
  <div class="hero-photo" role="img" aria-label="Photo of a smiling woman working on a laptop in a warm living room"></div>
  <div class="hero-shade"></div>
  <div class="topbar"></div>
  <div class="logo">Velmora</div>
  <nav class="nav">
    <a style="left:548px">Home</a>
    <a style="left:630px">About Us</a>
    <a style="left:734px">What We Do</a>
    <a style="left:862px">Blog</a>
    <a style="left:936px">Contact Us</a>
  </nav>
  <a class="login">Login</a>
  <h1 class="hero-title">Welcome to Velmora</h1>
  <p class="hero-text">Mentoring, volunteering and teamwork programs that people actually show up for. We bring the consulting, the training and the tools, and we make them fit what you already run.</p>
  <a class="btn btn-signup">SIGN UP FREE</a>
  <a class="btn btn-contact">CONTACT</a>
  <svg class="abs" style="left:38px;top:320px" width="22" height="22" viewBox="0 0 22 22"><circle cx="11" cy="11" r="11" fill="#fff"/><path d="M13 6l-5 5 5 5" fill="none" stroke="#333" stroke-width="2.4"/></svg>
  <svg class="abs" style="left:1148px;top:320px" width="22" height="22" viewBox="0 0 22 22"><circle cx="11" cy="11" r="11" fill="#fff"/><path d="M9 6l5 5-5 5" fill="none" stroke="#333" stroke-width="2.4"/></svg>
  <div class="dots"><span></span><span class="on"></span><span></span></div>
</header>

<section class="about">
  <h2 class="section-title" style="top:698px">ABOUT VELMORA</h2>
  <div class="title-rule" style="top:749px"></div>
  <div class="about-copy">
    <p>Your board asked for more engagement, better retention and real collaboration. Nobody told you where to start. That is where we come in. Velmora is a solutions company: we sit down with your directors and program managers, shape a mentoring or skills-based volunteering program around your people, train the ones who run it, and give them a tool that removes work instead of adding it. Your IT team gets a platform that connects to the systems you already trust, not another island to babysit.</p>
    <p>We care less about features and more about the moment two people meet and something good happens. Start small with one program, prove it works, then grow it across the whole organisation at your own pace.</p>
  </div>
  <a class="btn btn-more">READ MORE</a>
</section>

<section class="we-are">
  <div class="abs" style="inset:0" role="img" aria-label="Overhead photo of a team working around a dark table with laptops and notebooks"></div>
  <h2 class="section-title" style="top:142px">WE ARE</h2>
  <div class="title-rule" style="top:192px;left:545px;width:110px"></div>
  <p class="quote-lead">"We don't sell software and walk away. We sit down with your people, find what is stuck, and stay until it moves."</p>

  <div class="role" style="left:81px">
    <div class="role-badge" style="background:var(--accent)">
      <svg width="80" height="80" viewBox="0 0 80 80" fill="none" stroke="#fff" stroke-width="3" stroke-linejoin="round"><rect x="12" y="26" width="56" height="38" rx="4"/><path d="M30 26v-8h20v8M12 42h56"/><rect x="35" y="38" width="10" height="8" fill="#fff"/></svg>
    </div>
    <h3>ENTREPRENEURS</h3>
    <p>We have launched programs from nothing, so we know how to start small and grow what works.</p>
    <a>Read More &gt;</a>
  </div>
  <div class="role" style="left:343px">
    <div class="role-badge" style="background:var(--red)">
      <svg width="80" height="80" viewBox="0 0 80 80" fill="none" stroke="#fff" stroke-width="3.5" stroke-linecap="round" stroke-linejoin="round"><path d="M26 24L10 40l16 16M54 24l16 16-16 16M46 18L34 62"/></svg>
    </div>
    <h3>PROGRAMMERS</h3>
    <p>We build tools that plug into the platforms you already run and stay out of IT's way.</p>
    <a>Read More &gt;</a>
  </div>
  <div class="role" style="left:605px">
    <div class="role-badge" style="background:var(--yellow)">
      <svg width="80" height="80" viewBox="0 0 80 80" fill="none" stroke="#fff" stroke-width="3" stroke-linejoin="round"><path d="M8 14h40v24H24l-10 9v-9H8z"/><path d="M54 30h18v24h-6v9l-10-9H34V44"/></svg>
    </div>
    <h3>CONSULTANTS</h3>
    <p>We turn vague goals into a clear plan, then train the people who will carry it forward.</p>
    <a>Read More &gt;</a>
  </div>
  <div class="role" style="left:866px">
    <div class="role-badge" style="background:var(--green)">
      <svg width="80" height="80" viewBox="0 0 80 80" fill="none" stroke="#fff" stroke-width="3.5" stroke-linecap="round" stroke-linejoin="round"><path d="M10 66h60"/><path d="M14 54l18-18 12 10 24-26"/><path d="M54 20h14v14"/></svg>
    </div>
    <h3>INVESTORS</h3>
    <p>We put our own money in first, so every hour and dollar has to earn a measurable return.</p>
    <a>Read More &gt;</a>
  </div>
</section>

<section class="blog">
  <h2 class="section-title" style="top:2022px">OUR BLOG</h2>
  <div class="title-rule" style="top:2075px"></div>

  <article class="blog-card" style="left:86px">
    <div class="blog-photo" role="img" aria-label="Photo of a man sitting in a sunlit field with a laptop" style="background:linear-gradient(160deg,#e8d36a,#9aa544 60%,#5f7a2c)"></div>
    <h4>Turning "get people to collaborate" into a real plan</h4>
    <div class="blog-meta"><span>02 June, 2017</span><span>Read more &gt;</span></div>
  </article>
  <article class="blog-card" style="left:347px">
    <div class="blog-photo" role="img" aria-label="Photo of a hand sketching an idea diagram on a brick wall" style="background:linear-gradient(160deg,#b9664f,#c9b9a8 55%,#6f6a66)"></div>
    <h4>Mentoring programs that survive their second year</h4>
    <div class="blog-meta"><span>02 June, 2017</span><span>Read more &gt;</span></div>
  </article>
  <article class="blog-card" style="left:609px">
    <div class="blog-photo" role="img" aria-label="Photo of a man in a blue shirt in front of a chalk sketch on a wall" style="background:linear-gradient(180deg,#6d6d68,#4c5a6a 60%,#3d6a9c)"></div>
    <h4>Skills-based volunteering your board will fund</h4>
    <div class="blog-meta"><span>01 June, 2017</span><span>Read more &gt;</span></div>
  </article>
  <article class="blog-card" style="left:871px">
    <div class="blog-photo" role="img" aria-label="Photo of a smiling man at a bright office desk" style="background:linear-gradient(160deg,#e9eef2,#a9c3dc 55%,#3d78b8)"></div>
    <h4>How a new tool earns a place in your IT stack</h4>
    <div class="blog-meta"><span>01 June, 2017</span><span>Read more &gt;</span></div>
  </article>
</section>

<section class="testimonial">
  <svg class="abs" style="left:16px;top:228px" width="16" height="28" viewBox="0 0 16 28"><path d="M13 2L3 14l10 12" fill="none" stroke="rgba(255,255,255,.75)" stroke-width="2.6"/></svg>
  <svg class="abs" style="left:1154px;top:228px" width="16" height="28" viewBox="0 0 16 28"><path d="M3 2l10 12L3 26" fill="none" stroke="rgba(255,255,255,.75)" stroke-width="2.6"/></svg>
  <div class="avatar" role="img" aria-label="Portrait photo of the client giving the testimonial"></div>
  <div class="divider"></div>
  <blockquote>"We were handed a goal of 'more engagement' and no idea where to begin. Velmora helped us shape a mentoring program, trained our coordinators and gave them a tool they enjoy. Six months in, more than half our staff have taken part, and our IT team never had to chase a single issue."</blockquote>
  <cite>- Dana K Whitfield.</cite>
</section>

<footer class="footer">
  <div class="social"><span></span><span></span><span></span></div>
  <nav>
    <a class="footer-nav" style="left:366px">Home</a>
    <a class="footer-nav" style="left:449px">About Us</a>
    <a class="footer-nav" style="left:554px">What We Do</a>
    <a class="footer-nav" style="left:682px">Blog</a>
    <a class="footer-nav" style="left:757px">Contact Us</a>
  </nav>
  <p class="copyright">Copyright &copy; 2017. Velmora. All rights reserved.</p>
</footer>

</body>
</html>
```